Business Card for TVK, logo files already created

Please, can you assist with creating a Business card the TVK graphics which are already listed on www.brinmoretech.example
The business card should be modern and upmarket, textured designs are welcome. Please feel free to express yourself and be very bold with your design.

Target Market(s)

Cyber Security

Industry/Entity Type

Information Technology

Contact Information for Business Card

Company Name
Name
Title
Mobile
Fax or Tel
email
url

Font styles to use
Serif
Sans Serif

Colors
3277b5
85acd3
ffffff

```html
<!DOCTYPE html>
<html lang="en">
<head>
<meta charset="utf-8">
<title>TVK Business Card</title>
<link href="https://fonts.googleapis.com/css2?family=Exo+2:wght@400;500;700;800&display=swap" rel="stylesheet">
<style>
  :root {
    --brand-blue: #2e4a9c;
    --brand-grey: #555a60;
    --ink: #333;
    --paper: #ffffff;
    --backdrop: #2b2e33;
    --rule: #6a6a6a;
  }
  * { box-sizing: border-box; margin: 0; padding: 0; }
  html, body { width: 1200px; height: 900px; overflow: hidden; }
  body {
    background: var(--backdrop);
    font-family: "Exo 2", sans-serif;
    position: relative;
  }
  .card {
    position: absolute;
    width: 560px;
    height: 320px;
    background: var(--paper);
    border-radius: 26px;
    overflow: hidden;
  }
  .card--front { left: 40px; top: 290px; }
  .card--back { left: 620px; top: 290px; }

  /* Front */
  .front-logo {
    position: absolute; left: 34px; top: 28px;
    display: flex; align-items: center; gap: 14px;
  }
  .brand-mark {
    font-weight: 800; font-size: 76px; line-height: 1;
    color: var(--brand-blue); letter-spacing: 2px;
  }
  .brand-square { width: 18px; height: 18px; background: var(--brand-grey); }
  .front-tagline {
    position: absolute; left: 290px; top: 52px; width: 240px;
    text-align: center; color: var(--brand-blue);
  }
  .front-tagline .company {
    font-weight: 700; font-size: 26px; letter-spacing: 1px; text-transform: uppercase;
  }
  .front-tagline .motto {
    font-size: 11.5px; letter-spacing: 1.5px; text-transform: uppercase;
    border-top: 1.5px solid var(--rule); padding-top: 4px; margin-top: 4px;
  }
  .person { position: absolute; left: 34px; top: 128px; }
  .person .name {
    font-weight: 700; font-size: 22px; color: var(--brand-grey);
    text-transform: uppercase; letter-spacing: 0.5px;
  }
  .person .title { font-size: 14px; color: var(--ink); }
  .divider {
    position: absolute; left: 110px; top: 176px; width: 420px;
    border-top: 1.5px solid var(--rule);
  }
  .address {
    position: absolute; left: 34px; top: 200px;
    font-size: 14px; color: var(--brand-blue); line-height: 1.35;
  }
  .contacts {
    position: absolute; right: 30px; top: 198px;
    list-style: none; font-size: 15px; color: var(--ink);
  }
  .contacts li {
    display: flex; justify-content: flex-end; align-items: center;
    gap: 8px; height: 24px;
  }
  .contacts .highlight { color: var(--brand-blue); }
  .contacts svg { width: 15px; height: 15px; fill: var(--brand-blue); flex: none; }

  /* Back */
  .back-band {
    position: absolute; left: 0; right: 0; bottom: 0; height: 26px;
    background: var(--brand-blue);
  }
  .notch {
    position: absolute; width: 32px; height: 32px; border-radius: 50%;
    background: var(--backdrop);
  }
  .notch--top { left: 264px; top: -16px; }
  .notch--bottom { left: 264px; bottom: -16px; }
  .back-logo {
    position: absolute; left: 0; right: 0; top: 44px;
    text-align: center; color: var(--brand-blue);
  }
  .back-logo .brand-mark { font-size: 110px; }
  .back-logo .company {
    font-weight: 700; font-size: 32px; letter-spacing: 1px;
    text-transform: uppercase; margin-top: 6px;
  }
  .back-logo .motto {
    display: inline-block; font-size: 13px; letter-spacing: 2px;
    text-transform: uppercase; border-top: 1.5px solid var(--rule);
    padding: 5px 10px 0; margin-top: 6px;
  }
</style>
</head>
<body>
  <section class="card card--front">
    <div class="front-logo">
      <span class="brand-mark">TVK</span>
      <span class="brand-square"></span>
    </div>
    <div class="front-tagline">
      <div class="company">Brinmore Tech</div>
      <div class="motto">Secure - Minded Systems</div>
    </div>
    <div class="person">
      <div class="name">Alden Marsh</div>
      <div class="title">Director</div>
    </div>
    <div class="divider"></div>
    <div class="address">Harlow Bay<br>Northshire Region</div>
    <ul class="contacts">
      <li>210. 555. 014
        <svg viewBox="0 0 16 16"><rect x="4" y="1" width="8" height="14" rx="1.5"/><rect x="6" y="3" width="4" height="8" fill="#fff"/></svg></li>
      <li>021.555.087
        <svg viewBox="0 0 16 16"><path d="M3 2h3l1 3-2 1a8 8 0 0 0 5 5l1-2 3 1v3a1 1 0 0 1-1 1A12 12 0 0 1 2 3a1 1 0 0 1 1-1z"/></svg></li>
      <li>contact@brinmoretech.example
        <svg viewBox="0 0 16 16"><rect x="1" y="3" width="14" height="10" rx="1"/><path d="M1.5 3.5l6.5 5.5 6.5-5.5" fill="none" stroke="#fff" stroke-width="1.2"/></svg></li>
      <li><span>www.<span class="highlight">brinmoretech</span>.example</span>
        <svg viewBox="0 0 16 16"><circle cx="8" cy="8" r="7"/><path d="M1 8h14M8 1v14M8 1c-4 4-4 10 0 14M8 1c4 4 4 10 0 14" fill="none" stroke="#fff" stroke-width="1"/></svg></li>
    </ul>
  </section>

  <section class="card card--back">
    <div class="notch notch--top"></div>
    <div class="back-logo">
      <div class="brand-mark">TVK</div>
      <div class="company">Brinmore Tech</div>
      <div class="motto">Secure - Minded Systems</div>
    </div>
    <div class="back-band"></div>
    <div class="notch notch--bottom"></div>
  </section>
</body>
</html>
```